Parity Skills Forum needs a brochure to attract participants to its trainings

We need a flyer for our EU-funded project called " Parity Skills Forum" and it aims at increasing and developing skills of researchers and university staff members who are implementing measures towards gender equality in their institutions through our offered training programs. The final design should communicate gender equality for Research and Innovation centres and universities. This flyer will be distributed during conferences and events to our audience (mainly gender experts, researchers, administrative staff of universities, etc.) in order to provide the basic information about the project and options to get involved in the different trainings. We are attaching files to provide you with the concrete information on our requirements:- PS Forum flyer content.ppt: includes the content we would like to include in the flyer. There is also the URL to the project website and the different social media channels. - Project logo.zip: the project logo and guidelines as we would like to use colors that belong to the project logo color range. - Partners' logos.zip: Logos that will be included- EU flag: You can download different resolution files of the flag here: https://unionvexa.org/about-union/emblems/banner_en -Regarding the images or graphics that you may include in the brochure we wouldn’t like to propose any because we do not want to limitate your imagination.

As it was not mentioned and we received a lot of questions about it, we prefer the flyer to be double-sided and in A5

Font styles to use
Serif
Sans Serif

Colors

Designer to choose colors to be used in the design.

Requirements
Nice to have
• At least 4 pages
Should not have
• We would not like to see as dominant colours the classic blue and pink.

```html
<!DOCTYPE html>
<html lang="en">
<head>
<meta charset="utf-8">
<title>Parity Skills Forum – Brochure</title>
<link rel="stylesheet" href="https://fonts.googleapis.com/css2?family=Oswald:wght@500&family=Roboto:wght@400;500&family=Roboto+Condensed:wght@400;700&display=swap">
<style>
:root{
  --crimson:#d5245b;
  --teal:#3dc0d8;
  --purple:#7b3f92;
  --ink:#333;
  --muted:#666;
  --paper:#ffffff;
  --panel:#ededed;
  --backdrop:#dcdcdc;
}
*{box-sizing:border-box;margin:0;padding:0}
html,body{width:765px;height:1200px;overflow:hidden}
body{background:var(--backdrop);font-family:'Roboto',Arial,sans-serif;color:var(--ink);position:relative}
.spread{position:absolute;left:62px;width:640px;height:486px;display:flex;box-shadow:0 6px 18px rgba(0,0,0,.18)}
.spread--outer{top:40px}
.spread--inner{top:640px}
.page{position:relative;width:320px;height:486px;overflow:hidden}
.page--grey{background:var(--panel)}
.page--white{background:var(--paper)}
.band{position:absolute;left:0;width:320px}
.band-title{position:absolute;left:14px;color:#fff;font-family:'Roboto Condensed',Arial,sans-serif;font-size:17px}
/* audience */
.audience{position:absolute;left:20px;top:52px;width:290px}
.audience h3{font-family:'Roboto Condensed',Arial,sans-serif;font-weight:700;font-size:10px;color:var(--crimson);letter-spacing:.5px;margin-top:8px;display:flex;align-items:center;gap:7px}
.audience h3::before{content:"";width:7px;height:7px;border:2px solid var(--crimson);flex:none}
.audience p{font-size:6.6px;color:var(--muted);line-height:1.4;margin-top:2px}
/* partners */
.partners{position:absolute;left:14px;top:236px;width:296px;display:grid;grid-template-columns:repeat(4,1fr);gap:12px 10px}
.partner-badge{height:24px;background:#c9c9c9;border-radius:3px}
.partner-badge.round{width:26px;border-radius:50%;justify-self:center;background:#9aa8b8}
/* contacts */
.contacts{position:absolute;left:14px;top:390px;width:300px;display:grid;grid-template-columns:auto auto auto;gap:8px 10px;font-size:8.5px}
.contact{display:flex;align-items:center;gap:4px}
.contact::before{content:"";width:9px;height:9px;border-radius:50%;background:var(--teal);flex:none}
.footer-note{position:absolute;left:0;bottom:0;width:320px;height:48px;background:var(--crimson);color:#f6d3de;font-size:7.6px;text-align:center;line-height:1.35;padding:10px 18px 0}
.footer-note b{color:#fff;font-weight:500}
/* cover */
.photo{position:absolute;left:0;top:0;width:320px}
.brand{position:absolute;left:92px;top:228px;display:flex;align-items:center;gap:8px}
.brand-square{width:28px;height:28px;background:var(--crimson)}
.brand-name{font-size:15px;color:var(--ink)}
.cover-title{position:absolute;left:0;width:320px;text-align:center;top:272px;font-family:'Oswald',Impact,sans-serif;color:var(--crimson);font-size:29px;letter-spacing:1px;line-height:1.1}
.cover-title small{display:block;font-family:'Roboto',Arial,sans-serif;font-size:19px;font-weight:400;letter-spacing:3px;margin-top:2px}
.tagline{position:absolute;left:16px;top:352px;width:294px;font-size:11.2px;letter-spacing:.8px;line-height:1.45;color:#222}
.rule{position:absolute;left:14px;top:412px;width:294px;height:1px;background:var(--crimson)}
.funding{position:absolute;left:14px;top:424px;display:flex;gap:8px;align-items:center;width:300px}
.flag-block{width:65px;height:44px;background:#1f3a8f;flex:none}
.funding p{font-size:7px;line-height:1.35;color:#222}
/* training */
.training-title{position:absolute;left:0;width:320px;text-align:center;top:20px;font-family:'Roboto Condensed',Arial,sans-serif;font-weight:700;font-size:22px;color:var(--crimson)}
.training-intro{position:absolute;left:16px;top:62px;width:290px;font-size:10px;letter-spacing:.6px;line-height:1.35}
.formats{position:absolute;left:14px;top:110px;width:292px;display:grid;grid-template-columns:1fr 1fr;row-gap:14px}
.format{text-align:center;font-size:8.5px;letter-spacing:.8px;text-transform:uppercase}
.format svg{display:block;margin:0 auto 6px;width:50px;height:46px}
.format--purple{color:var(--purple)}
.format--teal{color:var(--teal)}
.format--crimson{color:var(--crimson)}
.more-offer{position:absolute;left:20px;bottom:14px;width:170px;color:#fff;text-align:center;font-size:7.4px;letter-spacing:1.4px;line-height:1.5}
.more-offer b{font-size:9.5px;font-weight:400;letter-spacing:2.4px}
.free-badge{position:absolute;left:192px;top:378px;width:110px;height:110px;border-radius:50%;background:var(--teal);border:6px solid var(--crimson);color:#fff;text-align:center;padding-top:28px;font-size:7.4px;letter-spacing:1px}
.free-badge strong{display:block;font-family:'Oswald',Impact,sans-serif;font-weight:500;font-size:18px;letter-spacing:2px;margin:2px 0}
.free-badge span{font-size:10px;letter-spacing:1.4px}
/* involve */
.involve-title{position:absolute;left:26px;top:288px;font-family:'Roboto Condensed',Arial,sans-serif;font-weight:700;font-size:18px;color:var(--crimson)}
.involve-list{position:absolute;left:20px;top:320px;width:290px;list-style:none}
.involve-list li{font-size:8.4px;letter-spacing:.7px;margin-bottom:9px;display:flex;gap:6px;align-items:center}
.involve-list li::before{content:"\2713";color:var(--crimson);font-weight:700;font-size:10px}
.visit{position:absolute;left:0;bottom:8px;width:320px;text-align:center;color:#fff;font-size:8.5px;letter-spacing:1.8px;line-height:2}
.visit b{font-size:11px;font-weight:400;letter-spacing:2.4px}
</style>
</head>
<body>

<section class="spread spread--outer">
  <article class="page page--grey">
    <svg class="band" style="top:0" width="320" height="52" viewBox="0 0 320 52">
      <polygon points="0,0 320,0 320,28 0,42" fill="var(--crimson)"/>
      <polygon points="130,36 320,28 320,36 200,41" fill="var(--teal)"/>
    </svg>
    <h2 class="band-title" style="top:12px">Who is it for?</h2>
    <div class="audience">
      <h3>Anyone interested in gender equality</h3>
      <h3>HR Professionals, Gender Trainers &amp; Experts</h3>
      <p>- Integration and establishment of gender-sensitive and fair recruitment and career management processes in organisations<br>- Train-the-trainers sessions for the development of new skills</p>
      <h3>Researchers &amp; Research Performing Organisations</h3>
      <p>- Training to integrate the gender dimension in their research and deepening their understanding of gender issues in R&amp;I<br>- Recommendations for influencing the internal policies and practices of the organisations towards gender equality</p>
    </div>
    <svg class="band" style="top:192px" width="320" height="40" viewBox="0 0 320 40">
      <polygon points="0,6 320,0 320,24 0,32" fill="var(--crimson)"/>
      <polygon points="200,27 320,24 320,32 260,33" fill="var(--teal)"/>
    </svg>
    <h2 class="band-title" style="top:200px">Our Partners</h2>
    <div class="partners">
      <div class="partner-badge"></div><div class="partner-badge"></div><div class="partner-badge round"></div><div class="partner-badge round"></div>
      <div class="partner-badge"></div><div class="partner-badge"></div><div class="partner-badge"></div><div class="partner-badge round"></div>
      <div class="partner-badge"></div><div class="partner-badge"></div><div class="partner-badge"></div><div class="partner-badge"></div>
    </div>
    <svg class="band" style="top:350px" width="320" height="40" viewBox="0 0 320 40">
      <polygon points="0,6 320,0 320,24 0,32" fill="var(--crimson)"/>
      <polygon points="200,27 320,24 320,32 260,33" fill="var(--teal)"/>
    </svg>
    <h2 class="band-title" style="top:358px">Contact Us</h2>
    <div class="contacts">
      <span class="contact">@PSForum_eu</span>
      <span class="contact">@PSForum.eu</span>
      <span class="contact">PS Forum</span>
      <span class="contact">info@ps-forum.eu</span>
      <span class="contact">www.ps-forum.eu</span>
    </div>
    <div class="footer-note">Do you still have questions? Feel free to contact us at <b>info@ps-forum.eu</b> A member of the team will make her/his best to reply as soon as possible.</div>
  </article>

  <article class="page page--white">
    <svg class="photo" width="320" height="212" viewBox="0 0 320 212" role="img" aria-label="Photo of people reading and writing at a wooden table">
      <defs><linearGradient id="tableTone" x1="0" y1="0" x2="1" y2="1"><stop offset="0" stop-color="#4d4a52"/><stop offset=".55" stop-color="#6f6a6e"/><stop offset="1" stop-color="#a9a5a0"/></linearGradient></defs>
      <rect width="320" height="212" fill="url(#tableTone)"/>
      <polygon points="0,158 320,188 320,212 0,212" fill="var(--paper)"/>
      <polygon points="0,154 320,182 320,200 0,176" fill="var(--crimson)"/>
      <polygon points="0,176 320,200 320,212 0,190" fill="var(--teal)"/>
    </svg>
    <div class="brand"><span class="brand-square"></span><span class="brand-name">PS Forum</span></div>
    <h1 class="cover-title">PARITY SKILLS<small>FORUM</small></h1>
    <p class="tagline">A high quality capacity building programme on gender equality in research, innovation and higher education</p>
    <div class="rule"></div>
    <div class="funding">
      <div class="flag-block" role="img" aria-label="Unionvexa flag"></div>
      <p>This project has received funding from the Unionvexa's Horizon Reach research and innovation programme under grant agreement No 731942.</p>
    </div>
  </article>
</section>

<section class="spread spread--inner">
  <article class="page page--grey">
    <h2 class="training-title">Training Offer</h2>
    <p class="training-intro">Find the format and training which suits you best and apply! Different dates and locations.</p>
    <div class="formats">
      <div class="format format--purple">
        <svg viewBox="0 0 50 46"><rect x="18" y="4" width="28" height="20" fill="none" stroke="var(--purple)" stroke-width="2.5"/><circle cx="10" cy="14" r="4" fill="var(--purple)"/><rect x="6" y="19" width="8" height="14" fill="var(--purple)"/><line x1="14" y1="21" x2="24" y2="14" stroke="var(--purple)" stroke-width="2"/><circle cx="24" cy="34" r="3" fill="var(--purple)"/><circle cx="34" cy="34" r="3" fill="var(--purple)"/><circle cx="44" cy="34" r="3" fill="var(--purple)"/><rect x="20" y="38" width="28" height="5" fill="var(--purple)"/></svg>
        In person-trainings
      </div>
      <div class="format format--crimson">
        <svg viewBox="0 0 50 46"><rect x="12" y="2" width="26" height="14" rx="2" fill="var(--crimson)"/><circle cx="25" cy="26" r="4" fill="var(--crimson)"/><circle cx="14" cy="30" r="4" fill="var(--crimson)"/><circle cx="36" cy="30" r="4" fill="var(--crimson)"/><rect x="8" y="36" width="34" height="8" rx="3" fill="var(--crimson)"/></svg>
        Workshops
      </div>
      <div class="format" style="color:#222">
        <svg viewBox="0 0 50 46"><polygon points="25,8 48,18 25,28 2,18" fill="#1e3345"/><path d="M12 23 v10 q13 8 26 0 v-10 l-13 6 z" fill="#1e3345"/></svg>
        Summer schools
      </div>
      <div class="format format--teal">
        <svg viewBox="0 0 50 46"><rect x="4" y="10" width="40" height="16" rx="8" fill="none" stroke="var(--teal)" stroke-width="3"/><circle cx="30" cy="22" r="7" fill="var(--paper)" stroke="var(--teal)" stroke-width="3"/><polyline points="26,28 26,40 30,36 34,40 34,28" fill="none" stroke="var(--teal)" stroke-width="2.5"/></svg>
        Doccs
      </div>
      <div class="format format--teal">
        <svg viewBox="0 0 50 46"><rect x="6" y="4" width="38" height="26" fill="none" stroke="var(--teal)" stroke-width="3"/><polygon points="21,10 21,24 32,17" fill="var(--teal)"/><line x1="25" y1="30" x2="16" y2="44" stroke="var(--teal)" stroke-width="3"/><line x1="25" y1="30" x2="34" y2="44" stroke="var(--teal)" stroke-width="3"/></svg>
        Webinars
      </div>
      <div class="format format--purple">
        <svg viewBox="0 0 50 46"><circle cx="10" cy="12" r="4" fill="var(--purple)"/><circle cx="40" cy="12" r="4" fill="var(--purple)"/><rect x="6" y="18" width="8" height="16" fill="var(--purple)"/><rect x="36" y="18" width="8" height="16" fill="var(--purple)"/><rect x="16" y="22" width="18" height="3" fill="var(--purple)"/><line x1="25" y1="25" x2="25" y2="40" stroke="var(--purple)" stroke-width="3"/><rect x="20" y="8" width="10" height="8" fill="none" stroke="var(--purple)" stroke-width="2"/></svg>
        Train the trainers<br>sessions
      </div>
    </div>
    <svg class="band" style="top:380px" width="320" height="106" viewBox="0 0 320 106">
      <path d="M0 26 Q60 -4 180 6 L320 20 L320 106 L0 106 Z" fill="var(--teal)"/>
      <path d="M0 44 Q60 14 180 22 L320 34 L320 106 L0 106 Z" fill="var(--crimson)"/>
    </svg>
    <p class="more-offer">for more offer<br>details please visit us at<br><b>www.ps-forum.eu</b></p>
    <div class="free-badge">PARTICIPATION IS<strong>FREE</strong><span>OF CHARGE</span></div>
  </article>

  <article class="page page--white">
    <svg class="photo" width="320" height="270" viewBox="0 0 320 270" role="img" aria-label="Group photo of training participants standing outside a building">
      <defs><linearGradient id="groupTone" x1="0" y1="0" x2="0" y2="1"><stop offset="0" stop-color="#d9dde0"/><stop offset=".45" stop-color="#9c8f86"/><stop offset="1" stop-color="#5b5a58"/></linearGradient></defs>
      <rect width="320" height="270" fill="url(#groupTone)"/>
      <polygon points="0,218 320,250 320,270 0,270" fill="var(--paper)"/>
      <polygon points="0,178 320,212 320,232 0,200" fill="var(--teal)"/>
      <polygon points="0,200 320,232 320,256 0,224" fill="var(--crimson)"/>
    </svg>
    <h2 class="involve-title">Get Involved</h2>
    <ul class="involve-list">
      <li>Take part in one or more offered trainings</li>
      <li>Become a gender trainer</li>
      <li>Become a host institution to the topic of your preference</li>
      <li>Be part of the pan European gender trainers' network</li>
    </ul>
    <svg class="band" style="top:420px" width="320" height="66" viewBox="0 0 320 66">
      <path d="M0 4 L260 4 Q310 4 320 30 L320 66 L0 66 Z" fill="var(--teal)"/>
      <path d="M0 16 L250 16 Q305 16 320 40 L320 66 L0 66 Z" fill="var(--crimson)"/>
    </svg>
    <p class="visit">Visit the website and find out more<br><b>www.ps-forum.eu</b></p>
  </article>
</section>

</body>
</html>
```